Business card design needed

We are a manufacturing business based in Archerfield, Brisbane, Queensland. We Insulate airconditioning ductwork and also manufacture some duct.
Updates

Hi guys, thanks for all the responses, they are looking really great

I have attached a couple of better quality photos of the products we use or manufacture, they don't "need" to be used in the card but i thought it was worth uploading them

I will be picking the final card in the next couple of days

Thanks for the response.

I think this will be the last update but i have included what we do so it can be added to the back of a card.

Target Market(s)

Local contractors

Industry/Entity Type

Business

Contact Information for Business Card

Korrin Insulation
Mark Delaney
87 Tullamore Road
Archerfield, QLD, 4108
mark@korrininsulation.example.com.au
Phone: 07 3914 2260

Requirements
Must have
• our logo which i have attached

Also, on the back of the card it would be nice to have what we do

-Duct lagging (internal and external)
-Manufacture of Z7 boxes
-Supply of glasswool, foam insulation, ductboard, foils, tapes & pins.

```html
<!DOCTYPE html>
<html lang="en">
<head>
<meta charset="utf-8">
<title>Korrin Insulation – Business Card</title>
<link rel="stylesheet" href="https://fonts.googleapis.com/css2?family=Roboto:wght@400;500&display=swap">
<style>
  :root {
    --stage: #7d7d7d;
    --card-dark-1: #3e4548;
    --card-dark-2: #1f2324;
    --card-light: #ffffff;
    --orange: #f08a24;
    --orange-deep: #e8652a;
    --amber: #ffd21f;
    --band-shadow: #9a9c9e;
    --band-shadow-dark: #5a5a5a;
    --ink: #3a3a3a;
    --ink-soft: #4a4a4a;
    --white: #ffffff;
  }
  * { box-sizing: border-box; margin: 0; padding: 0; }
  html, body {
    width: 1200px; height: 900px; overflow: hidden;
    background: var(--stage);
    font-family: "Roboto", Arial, sans-serif;
  }
  .card {
    position: absolute; top: 291px;
    width: 490px; height: 298px; overflow: hidden;
  }
  .card-front {
    left: 98px;
    background: radial-gradient(ellipse at 45% 35%, var(--card-dark-1), var(--card-dark-2) 85%);
  }
  .card-back { left: 624px; background: var(--card-light); }
  .card-band { position: absolute; inset: 0; }
  .brand {
    position: absolute; display: flex; align-items: center; gap: 8px;
    font-weight: 500; font-size: 21px; letter-spacing: 0.5px;
    text-transform: uppercase; white-space: nowrap;
  }
  .brand-mark { width: 16px; height: 16px; background: var(--orange); }
  .card-front .brand { left: 28px; top: 214px; color: var(--white); }
  .card-back .brand { right: 28px; top: 42px; color: var(--ink); }
  .contact {
    position: absolute; right: 22px; top: 166px;
    text-align: right; color: var(--ink-soft);
  }
  .contact-name { font-weight: 500; font-size: 15px; letter-spacing: 0.6px; color: var(--ink); }
  .contact-role { font-size: 9px; letter-spacing: 0.4px; margin-top: 5px; margin-bottom: 15px; }
  .contact-line {
    display: flex; justify-content: flex-end; align-items: center; gap: 5px;
    font-size: 12px; line-height: 16px; white-space: nowrap;
  }
  .contact-line svg { width: 11px; height: 11px; flex: none; }
  .contact-line.address { padding-right: 16px; }
</style>
</head>
<body>

<section class="card card-front" aria-label="Card front">
  <svg class="card-band" viewBox="0 0 490 298" aria-hidden="true">
    <defs>
      <linearGradient id="band-front" x1="0" y1="1" x2="1" y2="0">
        <stop offset="0" stop-color="var(--amber)"/>
        <stop offset="0.5" stop-color="var(--orange)"/>
        <stop offset="1" stop-color="var(--orange-deep)"/>
      </linearGradient>
    </defs>
    <polygon points="196,298 262,298 490,70 490,4" fill="var(--band-shadow)"/>
    <polygon points="218,298 290,298 490,98 490,26" fill="url(#band-front)"/>
  </svg>
  <div class="brand"><span class="brand-mark"></span>Korrin Insulation</div>
</section>

<section class="card card-back" aria-label="Card back">
  <svg class="card-band" viewBox="0 0 490 298" aria-hidden="true">
    <defs>
      <linearGradient id="band-back" x1="1" y1="1" x2="0" y2="0">
        <stop offset="0" stop-color="var(--orange-deep)"/>
        <stop offset="1" stop-color="var(--orange)"/>
      </linearGradient>
    </defs>
    <polygon points="33,0 76,0 242,190 14,298 0,298 0,276 190,186 47,20" fill="var(--band-shadow-dark)"/>
    <polygon points="19,0 62,0 228,190 0,298 0,250 176,180" fill="url(#band-back)"/>
  </svg>
  <div class="brand"><span class="brand-mark"></span>Korrin Insulation</div>
  <div class="contact">
    <p class="contact-name">MARK DELANEY</p>
    <p class="contact-role">PRESIDENT</p>
    <p class="contact-line address">87 Tullamore Road Archerfield, QLD, 4108</p>
    <p class="contact-line">07 3914 2260
      <svg viewBox="0 0 12 12" aria-hidden="true"><path d="M2 1l2 0 1 3-1.3 1a7 7 0 0 0 3.3 3.3L8 7l3 1 0 2c0 .6-.5 1-1 1A9 9 0 0 1 1 2c0-.5.4-1 1-1z" fill="var(--orange)"/></svg>
    </p>
    <p class="contact-line">mark@korrininsulation.example.com.au
      <svg viewBox="0 0 12 12" aria-hidden="true"><rect x="1" y="3" width="10" height="7" rx="1" fill="var(--orange)"/><path d="M1.5 3.5L6 7l4.5-3.5" stroke="#fff" fill="none"/></svg>
    </p>
    <p class="contact-line">www.korrininsulation.example.com.au
      <svg viewBox="0 0 12 12" aria-hidden="true"><circle cx="6" cy="6" r="5" fill="var(--orange)"/><path d="M1 6h10M6 1c-2.5 3-2.5 7 0 10M6 1c2.5 3 2.5 7 0 10" stroke="#fff" stroke-width=".8" fill="none"/></svg>
    </p>
  </div>
</section>

</body>
</html>
```